nutrition company business card

I would like to have a business card that has two sides, one being the green color from the Company name on the logo. I am open to ideas and looks that work with my logo. I like the idea of having a negative image of the tree on the green side.

For my information on the card I must have:
Linda Moorcombe
415-872-6041
lindamoorcombe@quellmail.net

This area will need to be updated once I complete my schooling.

Reason: I need to extend my deadline by one day as I have been sick the last week and not had time to review all the new designs. Thank you.

Industry/Entity Type

Nutrition

Requirements
Must have
• I would like to have a business card that has two sides, one being the green color from the Company name on the logo. I am open to ideas and looks that work with my logo. I like the idea of having a negative image of the tree on the green side.
• For my information on the card I must have:
• Linda Moorcombe
• 415-872-6041
• lindamoorcombe@quellmail.net
• This area will need to be updated once I complete my schooling.

```html
<!DOCTYPE html>
<html lang="en">
<head>
<meta charset="utf-8">
<title>Thriving Tables – Business Card</title>
<link rel="stylesheet" href="https://fonts.googleapis.com/css2?family=Quicksand:wght@400;500;600&display=swap">
<style>
  :root {
    --leaf-green: #72b62e;
    --leaf-green-deep: #5fa024;
    --leaf-green-light: #8cc84b;
    --bark-brown: #6b5246;
    --paper: #f7f7f5;
    --ink: #3d3d3d;
    --ink-soft: #7c7c7c;
    --backdrop: #e8e5e0;
  }
  * { box-sizing: border-box; margin: 0; padding: 0; }
  html, body {
    width: 1200px;
    height: 723px;
    overflow: hidden;
    background: var(--backdrop);
    font-family: "Quicksand", sans-serif;
  }
  .card-spread {
    position: relative;
    width: 1200px;
    height: 723px;
    display: flex;
    justify-content: center;
    align-items: center;
    gap: 60px;
  }
  .card {
    position: relative;
    width: 340px;
    height: 595px;
    border-radius: 4px;
    overflow: hidden;
    box-shadow: 0 10px 28px rgba(60, 50, 40, 0.18);
  }

  /* Back side */
  .card--back {
    background: linear-gradient(160deg, var(--leaf-green-light) 0%, var(--leaf-green) 55%, var(--leaf-green-deep) 100%);
  }
  .card--back .tree-mark {
    position: absolute;
    left: 50%;
    top: 50%;
    width: 230px;
    height: 230px;
    transform: translate(-50%, -50%);
    border-radius: 50%;
    background: rgba(80, 140, 25, 0.35);
  }

  /* Front side */
  .card--front {
    background: var(--paper);
  }
  .card__edge {
    position: absolute;
    left: 0;
    width: 100%;
    display: block;
  }
  .card__edge--top { top: 0; height: 60px; }
  .card__edge--bottom { bottom: 0; height: 90px; }

  .brand {
    position: absolute;
    top: 34px;
    left: 0;
    width: 100%;
    padding: 0 26px;
  }
  .brand__mark {
    display: block;
    width: 96px;
    height: 96px;
    margin: 0 42px 10px auto;
    border-radius: 50%;
    border: 5px solid var(--bark-brown);
    background: #fff;
  }
  .brand__name {
    font-size: 33px;
    font-weight: 500;
    color: var(--leaf-green);
    line-height: 1.05;
    letter-spacing: 0.3px;
  }
  .brand__tagline {
    margin-top: 3px;
    font-size: 16px;
    font-weight: 500;
    color: var(--ink-soft);
    letter-spacing: 1.2px;
    white-space: nowrap;
  }

  .contact {
    position: absolute;
    top: 262px;
    left: 0;
    width: 100%;
    list-style: none;
    text-align: center;
  }
  .contact__item {
    margin-bottom: 26px;
  }
  .contact__icon {
    display: block;
    width: 34px;
    height: 34px;
    margin: 0 auto 8px;
    border-radius: 50%;
    background: var(--leaf-green);
  }
  .contact__icon svg { display: block; width: 34px; height: 34px; }
  .contact__text {
    font-size: 18px;
    font-weight: 500;
    color: var(--ink);
    letter-spacing: 0.4px;
  }
</style>
</head>
<body>
<main class="card-spread">

  <section class="card card--back" aria-label="Card back">
    <div class="tree-mark" role="img" aria-label="Faint tone-on-tone tree emblem"></div>
  </section>

  <section class="card card--front" aria-label="Card front">
    <svg class="card__edge card__edge--top" viewBox="0 0 340 60" preserveAspectRatio="none" aria-hidden="true">
      <path d="M230 0 H340 V48 C310 20 275 6 230 0 Z" fill="var(--leaf-green)"/>
    </svg>

    <header class="brand">
      <span class="brand__mark" aria-hidden="true"></span>
      <h1 class="brand__name">Thriving Tables</h1>
      <p class="brand__tagline">simple meals for busy homes</p>
    </header>

    <ul class="contact">
      <li class="contact__item">
        <span class="contact__icon">
          <svg viewBox="0 0 34 34" aria-hidden="true">
            <circle cx="17" cy="13" r="4.5" fill="#fff"/>
            <path d="M9 25 C9 19.5 12.5 18 17 18 C21.5 18 25 19.5 25 25 Z" fill="#fff"/>
          </svg>
        </span>
        <p class="contact__text">Linda Moorcombe</p>
      </li>
      <li class="contact__item">
        <span class="contact__icon">
          <svg viewBox="0 0 34 34" aria-hidden="true">
            <rect x="12.5" y="8" width="9" height="18" rx="2" fill="#fff"/>
            <rect x="14" y="10.5" width="6" height="7" fill="var(--leaf-green)"/>
            <circle cx="17" cy="22" r="1.3" fill="var(--leaf-green)"/>
          </svg>
        </span>
        <p class="contact__text">415-872-6041</p>
      </li>
      <li class="contact__item">
        <span class="contact__icon">
          <svg viewBox="0 0 34 34" aria-hidden="true">
            <rect x="9" y="11" width="16" height="12" rx="1" fill="#fff"/>
            <path d="M9.5 11.5 L17 18 L24.5 11.5" fill="none" stroke="var(--leaf-green)" stroke-width="1.4"/>
          </svg>
        </span>
        <p class="contact__text">lindamoorcombe@quellmail.net</p>
      </li>
    </ul>

    <svg class="card__edge card__edge--bottom" viewBox="0 0 340 90" preserveAspectRatio="none" aria-hidden="true">
      <path d="M0 20 C90 60 220 85 340 72 V90 H0 Z" fill="var(--leaf-green)"/>
    </svg>
  </section>

</main>
</body>
</html>
```